Harborline Security and Surveillance Business Card

Business Card Design - Company Name:Freedom Security and SurveillanceWe are a Security Systems Integrator Specializing in Security Systems/ Video Surveillance and Access Control. Our areas of expertise are:Security SystemsVideo SurveillanceAccess ControlFire Alarm SystemsNetwork CablingCellular BoostersMy input is the Front of the Card is: logo, name of Business, My Name, Phone Number, and email.Rear of Card is the 6 areas of expertise, I just dont want the front to be very busy.
Name: Tom Werner
Title: President
Email: tom@harborlinesecsys.example
website: harborlinesecsys.example

```html
<!DOCTYPE html>
<html lang="en">
<head>
<meta charset="utf-8">
<title>Harborline Security and Surveillance Business Card</title>
<link href="https://fonts.googleapis.com/css2?family=Arimo:wght@400;700&display=swap" rel="stylesheet">
<style>
  :root {
    --stage: #2b2b2d;
    --card: #f4f4f5;
    --card-edge: #e2e2e4;
    --brand-blue: #1a5fc0;
    --steel: #8e9196;
    --ink: #3a3d42;
    --white: #ffffff;
  }
  * { margin: 0; padding: 0; box-sizing: border-box; }
  html, body { width: 1200px; height: 997px; overflow: hidden; }
  body {
    background: var(--stage);
    font-family: "Arimo", Arial, sans-serif;
    display: flex;
    align-items: center;
    justify-content: center;
    gap: 40px;
  }
  .card {
    position: relative;
    width: 540px;
    height: 309px;
    background: linear-gradient(180deg, var(--white), var(--card));
    border-radius: 18px;
    overflow: hidden;
    box-shadow: 0 10px 30px rgba(0,0,0,.45);
  }

  /* Back side */
  .card--back { display: flex; align-items: center; justify-content: center; }
  .brand-lockup { display: flex; flex-direction: column; align-items: center; gap: 14px; }
  .brand-mark { width: 54px; height: 54px; border-radius: 50%; background: var(--brand-blue); }
  .brand-name {
    color: var(--brand-blue);
    font-weight: 700;
    text-transform: uppercase;
    text-align: center;
    letter-spacing: 3px;
    font-size: 30px;
    line-height: 1.15;
  }
  .brand-name small { display: block; font-size: 15px; letter-spacing: 7px; }
  .brand-rule { width: 420px; height: 2px; background: var(--steel); }

  /* Front side */
  .front-header { position: absolute; top: 30px; left: 28px; display: flex; align-items: center; gap: 14px; }
  .front-header .brand-mark { width: 46px; height: 46px; }
  .front-header .brand-name { font-size: 23px; letter-spacing: 2px; text-align: left; }
  .front-header .brand-name small { font-size: 12px; letter-spacing: 6px; }

  .contact { position: absolute; top: 112px; left: 150px; width: 300px; }
  .contact-name { color: var(--brand-blue); font-weight: 700; font-size: 15px; letter-spacing: .5px; text-align: center; padding-right: 70px; }
  .contact-title { color: var(--ink); font-size: 11px; text-align: center; padding-right: 70px; }
  .contact-phone { position: absolute; right: 0; top: 12px; font-size: 11px; color: var(--ink); display: flex; align-items: center; gap: 4px; }
  .contact-rule { height: 2px; background: var(--brand-blue); margin: 5px 0 5px; }
  .contact-email { font-size: 11px; color: var(--ink); display: flex; align-items: center; gap: 4px; }
  .icon { width: 9px; height: 9px; fill: var(--brand-blue); }

  .expertise { position: absolute; left: 0; right: 0; bottom: 0; height: 110px; }
  .expertise-rule { position: absolute; top: 16px; left: 0; right: 0; height: 3px; background: var(--steel); }
  .expertise-label {
    position: absolute; top: 5px; left: 50%; transform: translateX(-50%);
    background: var(--steel); color: var(--white);
    font-size: 12px; padding: 3px 14px; border-radius: 12px;
  }
  .expertise-band {
    position: absolute; top: 34px; left: 0; right: 0; bottom: 12px;
    background: var(--brand-blue);
    display: flex; flex-direction: column; justify-content: center; gap: 8px;
    padding-left: 22px;
  }
  .expertise-row { display: flex; gap: 16px; list-style: none; }
  .expertise-row li { color: var(--white); font-size: 12.5px; letter-spacing: .4px; text-transform: uppercase; }
  .expertise-row li::before { content: "● "; font-size: 10px; }
  .expertise-foot { position: absolute; bottom: 0; left: 0; right: 0; height: 12px; background: var(--card-edge); }
</style>
</head>
<body>

  <section class="card card--back" aria-label="Card back">
    <div class="brand-lockup">
      <div class="brand-mark"></div>
      <div class="brand-name">Harborline Security<small>and Surveillance</small></div>
      <div class="brand-rule"></div>
    </div>
  </section>

  <section class="card card--front" aria-label="Card front">
    <header class="front-header">
      <div class="brand-mark"></div>
      <div class="brand-name">Harborline Security<small>and Surveillance</small></div>
    </header>

    <div class="contact">
      <p class="contact-name">DALE HUTCHINS</p>
      <p class="contact-title">Director</p>
      <p class="contact-phone">
        <svg class="icon" viewBox="0 0 10 10"><rect x="1" y="2" width="8" height="6" rx="1"/></svg>
        555-014-2290
      </p>
      <div class="contact-rule"></div>
      <p class="contact-email">
        <svg class="icon" viewBox="0 0 10 10"><path d="M2 1h2l1 2-1.2 1a5 5 0 0 0 2.2 2.2L7 5l2 1v2a1 1 0 0 1-1 1A7 7 0 0 1 1 2a1 1 0 0 1 1-1z"/></svg>
        info@harborlinesecsys.example
      </p>
    </div>

    <div class="expertise">
      <div class="expertise-rule"></div>
      <span class="expertise-label">Our Areas of Expertise</span>
      <div class="expertise-band">
        <ul class="expertise-row">
          <li>Security Systems</li><li>Video Surveillance</li><li>Access Control</li>
        </ul>
        <ul class="expertise-row">
          <li>Fire Alarm Systems</li><li>Network Cabling</li><li>Cellular Boosters</li>
        </ul>
      </div>
      <div class="expertise-foot"></div>
    </div>
  </section>

</body>
</html>
```